BRYLTAllies.co.uk - Mental Health Clinic for Child and Adolescents

Updated 29/01/2018***
I am not sure you guys are getting the idea regards to the opening page / homescreen layout. Can you look at the new images I have uploaded (page 5, 6 and 7) These are some of the layouts I like but to incorporate my chosen images, with the BRYLT commissioner, buttons and a sliding header bar.
I have written a strong brief, I am looking for a website, preferably wordpress as i know they are easy to maintain. I am looking for a one page site, with the top / opening page being full screen image with drop down categories. I have made a rough design, see full brief in word doc attached, there is some freedom to play around with the design aspect but it will need to relay all the content provided. I like a minimal feel. I have also attached some images that may be useful, but will need a new logo for BRYLT Allies. I have attached some logo idea's, it is up to you decide whether you want to use them.
I would prefer the homepage as full screen image, and the categories offered as a drop down or over the main image.
I have also attached linked to some competitors websites:
https://www.verdano-group.co.uk/
http://www.qwmr.org.uk/
Industry/Entity Type
Clinic
Number of Pages Required
1 page
Font styles to use
Look and feel
Each slider illustrates characteristics of the customer's brand and the style your logo design should communicate.

```html
<!DOCTYPE html>
<html lang="en">
<head>
<meta charset="UTF-8">
<title>Our Therapies</title>
<link rel="stylesheet" href="https://fonts.googleapis.com/css2?family=Open+Sans:wght@400;700&display=swap">
<style>
  :root {
    --page-bg: #e8e8e8;
    --band-bg: #f1f1f1;
    --edge: #2f3a3f;
    --heading: #263238;
    --body-text: #2b2f31;
    --rule: #2f3a3f;
  }
  * { margin: 0; padding: 0; box-sizing: border-box; }
  html, body { width: 1200px; height: 1200px; overflow: hidden; }
  body {
    position: relative;
    background: var(--page-bg);
    font-family: "Open Sans", Arial, sans-serif;
    color: var(--body-text);
  }
  .page-edge {
    position: absolute; left: 0; top: 0; width: 4px; height: 1200px;
    background: var(--edge);
  }
  .service-band { position: absolute; left: 4px; width: 1196px; }
  .band-cbt { top: 0; height: 426px; background: var(--page-bg); }
  .band-emdr { top: 426px; height: 430px; background: var(--band-bg); }
  .band-family { top: 856px; height: 344px; background: var(--page-bg); }

  .service-photo { position: absolute; display: block; }
  .photo-cbt {
    left: 4px; top: 0; width: 575px; height: 426px;
    background: linear-gradient(100deg, #6b8a86 0%, #c9c3bb 22%, #e9e6e1 45%, #f2f1ee 60%, #d9d2c8 85%, #9c7b5e 100%);
  }
  .photo-emdr {
    left: 622px; top: 428px; width: 576px; height: 422px;
    background: linear-gradient(95deg, #6c7f94 0%, #8ea0b3 25%, #c9bfae 55%, #d8cfc0 75%, #e9e6df 100%);
  }
  .photo-family {
    left: 4px; top: 858px; width: 575px; height: 342px;
    background: linear-gradient(100deg, #6b8a86 0%, #c9c3bb 22%, #e9e6e1 45%, #f2f1ee 60%, #d9d2c8 85%, #9c7b5e 100%);
  }

  .service-copy { position: absolute; width: 508px; }
  .copy-cbt { left: 626px; top: 23px; }
  .copy-emdr { left: 58px; top: 466px; width: 509px; }
  .copy-family { left: 626px; top: 886px; }

  .service-title {
    font-size: 31px; line-height: 34px; font-weight: 700;
    color: var(--heading); letter-spacing: 0.3px;
    padding: 0 0 4px 1px;
    border-bottom: 2px solid var(--rule);
  }
  .service-intro {
    margin-top: 7px; padding-left: 1px;
    font-size: 19px; line-height: 28.8px;
  }
  .copy-emdr .service-intro { margin-top: 12px; padding-left: 2px; width: 505px; }
  .copy-family .service-intro { margin-top: 6px; }

  .condition-list { list-style: none; margin-top: 14px; }
  .copy-emdr .condition-list { margin-top: 22px; }
  .copy-family .condition-list { margin-top: 15px; }
  .condition-list li {
    position: relative; padding-left: 43px;
    font-size: 19px; line-height: 28.8px;
  }
  .condition-list li::before {
    content: ""; position: absolute; left: 8px; top: 13px;
    width: 4px; height: 4px; border-radius: 50%;
    background: var(--body-text);
  }
</style>
</head>
<body>
  <div class="page-edge"></div>

  <section class="service-band band-cbt">
    <div class="service-photo photo-cbt" role="img" aria-label="Photo of a therapist in a white shirt talking with a teenage boy by a white brick fireplace"></div>
  </section>
  <div class="service-copy copy-cbt">
    <h2 class="service-title">CBT</h2>
    <p class="service-intro">We can offer high quality that will be carried out by either a qualified psychological wellbeing practitioner or a NACTB accredited CBT therapist. Our therapists are trained to work with the following:</p>
    <ul class="condition-list">
      <li>Anxiety and Depression</li>
      <li>Eating Disorders</li>
      <li>Trauma</li>
      <li>Body Dysmorphia</li>
      <li>Addiction</li>
    </ul>
  </div>

  <section class="service-band band-emdr"></section>
  <div class="service-photo photo-emdr" role="img" aria-label="Photo of a smiling therapist in a denim shirt sitting on a sofa with a young girl"></div>
  <div class="service-copy copy-emdr">
    <h2 class="service-title">EMDR</h2>
    <p class="service-intro">We can offer high quality that will be carried out by fully qualified EMDR therapist. Our therapists are trained to work with the following:</p>
    <ul class="condition-list">
      <li>Anxiety and Depression</li>
      <li>Eating Disorders</li>
      <li>Trauma</li>
      <li>Body Dysmorphia</li>
      <li>Addiction</li>
    </ul>
  </div>

  <section class="service-band band-family"></section>
  <div class="service-photo photo-family" role="img" aria-label="Photo of a therapist in a white shirt talking with a teenage boy by a white brick fireplace"></div>
  <div class="service-copy copy-family">
    <h2 class="service-title">Family Therapists</h2>
    <p class="service-intro">We can offer high quality that will be carried out by fully qualified Family Therapists therapist. Our therapists are trained to work with the following:</p>
    <ul class="condition-list">
      <li>Anxiety and Depression</li>
      <li>Eating Disorders</li>
      <li>Trauma</li>
      <li>Body Dysmorphia</li>
      <li>Addiction</li>
    </ul>
  </div>
</body>
</html>
```